依頼詳細
〇 ターゲット
地域の求職者(看護師、理学療法士、作業療法士)

〇 掲載方法
地域の福祉フリーペーの裏表紙(https://k-tomo-ne.jp/pompom/index.html

〇 納期
本当は明日まででしたが、早いと助かります。

〇 内容
添付データを参照ください。
シンプルテイストにロゴとコンセプトから―を絡めていただければと思います。

〇納品データ
トンボ付き入稿データ(PDF、ai.)
印刷機で印刷できるPDFデータ(トンボなし)
記載項目
ロゴ:添付(はな訪問看護ステーション森岡の「飯塚」「iizuka」の文字部分を削除して中央位置の訂正お願いします)
内容:添付
サイズ
A4
ページ数
片面
希望イメージ
シンプル 複雑
単色 カラフル
暗い 明るい
日常 高級
遊び心 厳粛
未来的 伝統的
女性的 男性的
希望する色
赤系
納品ファイル
• イラストレーター形式 (.ai)
補足説明

業務内容がシンプルにまとめられており、応募効果が高そうであると判断しました

短期間でたくさんのご提案ありがとうございました。
また、機会がございましたら、よろしくお願いします。

```html
<!DOCTYPE html>
<html lang="ja">
<head>
<meta charset="UTF-8">
<title>訪問看護師 大募集</title>
<link href="https://fonts.googleapis.com/css2?family=Noto+Sans+JP:wght@400;500;700;900&family=Zen+Maru+Gothic:wght@500;700;900&display=swap" rel="stylesheet">
<style>
  :root {
    --orange: #f39a3a;
    --orange-deep: #ee7d1f;
    --red: #e5412b;
    --brown: #4a3328;
    --white: #ffffff;
    --blue: #2b5fb8;
    --photo-top: #f3efe9;
    --photo-bottom: #e6d8c8;
  }
  * { margin: 0; padding: 0; box-sizing: border-box; }
  html, body { width: 857px; height: 1200px; overflow: hidden; background: var(--white); }
  .poster {
    position: relative; width: 857px; height: 1200px; overflow: hidden;
    font-family: "Noto Sans JP", sans-serif; color: var(--brown);
  }
  .hero-photo {
    position: absolute; left: 0; top: 0; width: 857px; height: 440px;
    background: linear-gradient(180deg, var(--photo-top), var(--photo-bottom));
  }
  .brand {
    position: absolute; left: 22px; top: 18px; display: flex; flex-direction: column; align-items: center; gap: 6px;
  }
  .brand-mark { width: 54px; height: 54px; border-radius: 50%; background: var(--red); }
  .brand-name { font-size: 12px; font-weight: 700; color: var(--red); }
  .tagline {
    position: absolute; left: 50%; top: 340px; transform: translateX(-50%);
    width: 670px; height: 76px; border-radius: 38px;
    background: var(--white); border: 3px solid var(--brown);
    display: flex; align-items: center; justify-content: center;
    font-family: "Zen Maru Gothic", sans-serif; font-weight: 700; font-size: 32px; letter-spacing: 1px;
  }
  .recruit-band {
    position: absolute; left: 0; top: 440px; width: 857px; height: 600px; background: var(--orange);
  }
  .recruit-card {
    position: absolute; left: 114px; top: 490px; width: 629px; height: 420px;
    background: var(--white); text-align: center;
    font-family: "Zen Maru Gothic", sans-serif;
  }
  .reason {
    margin: 34px auto 0; display: flex; align-items: center; justify-content: center; gap: 16px;
    font-size: 34px; font-weight: 700; color: var(--brown);
  }
  .reason::before, .reason::after { content: ""; width: 3px; height: 40px; background: var(--brown); }
  .reason::before { transform: rotate(-25deg); }
  .reason::after { transform: rotate(25deg); }
  .job-title { margin-top: 18px; font-size: 82px; font-weight: 900; color: var(--orange-deep); letter-spacing: 6px; line-height: 1.1; }
  .job-call { margin-top: 14px; font-size: 64px; font-weight: 900; color: var(--red); letter-spacing: 4px; line-height: 1.1; }
  .job-others { margin-top: 20px; font-size: 27px; font-weight: 700; color: var(--brown); }
  .walkers {
    position: absolute; left: 230px; top: 925px; width: 100px; height: 105px;
    background: linear-gradient(180deg, #f7b46a, #e98a2a); border-radius: 8px;
  }
  .urgent-sign { position: absolute; left: 350px; top: 915px; width: 140px; height: 110px; }
  .urgent-label {
    position: absolute; left: 0; bottom: 0; width: 140px; height: 58px;
    background: var(--white); border: 3px solid var(--brown);
    display: flex; align-items: center; justify-content: center;
    font-family: "Zen Maru Gothic", sans-serif; font-weight: 900; font-size: 30px; color: var(--red);
  }
  .footer-search { position: absolute; left: 36px; top: 1064px; display: flex; align-items: center; gap: 12px; }
  .job-site { font-size: 22px; font-weight: 700; color: var(--blue); }
  .search-box {
    width: 310px; height: 44px; border: 3px solid var(--orange); border-radius: 6px;
    display: flex; align-items: center; justify-content: space-between; padding: 0 10px;
    font-size: 19px; font-weight: 700;
  }
  .search-suffix { font-size: 22px; font-weight: 700; }
  .contact {
    position: absolute; left: 36px; top: 1126px; font-size: 15px; line-height: 1.45;
    font-weight: 500; font-style: normal;
  }
  .contact strong { font-size: 16px; }
  .car {
    position: absolute; left: 612px; top: 1050px; width: 230px; height: 140px;
    background: linear-gradient(180deg, #f6f6f6, #dcdcdc); border-radius: 40px 50px 12px 12px;
  }
</style>
</head>
<body>
<main class="poster">
  <div class="hero-photo" role="img" aria-label="笑顔の看護師が高齢の女性の手を握る写真"></div>
  <div class="brand">
    <span class="brand-mark"></span>
    <span class="brand-name">はな訪問看護ステーション</span>
  </div>
  <p class="tagline">あなたも一緒に、笑顔を作りませんか？</p>

  <section class="recruit-band"></section>
  <section class="recruit-card">
    <p class="reason">利用者急増につき</p>
    <h1 class="job-title">訪問看護師</h1>
    <p class="job-call">大募集!!</p>
    <p class="job-others">他、理学療法士、作業療法士も募集中!</p>
  </section>

  <div class="walkers" role="img" aria-label="歩く人々の小さなイラスト"></div>

  <div class="urgent-sign">
    <svg width="140" height="56" viewBox="0 0 140 56">
      <polyline points="20,56 70,4 120,56" fill="none" stroke="#4a3328" stroke-width="3"/>
      <circle cx="70" cy="4" r="4" fill="#4a3328"/>
    </svg>
    <div class="urgent-label">急募</div>
  </div>

  <div class="footer-search">
    <span class="job-site">ジョブナビ</span>
    <div class="search-box">
      <span>はな訪問看護ステーション</span>
      <svg width="24" height="24" viewBox="0 0 26 26"><circle cx="11" cy="11" r="7" fill="none" stroke="#4a3328" stroke-width="3"/><line x1="16" y1="16" x2="23" y2="23" stroke="#4a3328" stroke-width="3"/></svg>
    </div>
    <span class="search-suffix">で検索!!</span>
  </div>

  <address class="contact">
    <strong>はな訪問看護ステーション</strong><br>
    森岡市花園町3丁目18-11<br>
    TEL：080-4172-3068（採用）
  </address>

  <div class="car" role="img" aria-label="訪問看護ステーションの白い軽自動車のイラスト"></div>
</main>
</body>
</html>
```